Best in class business looking for best in class stationery that accurately reflects the brand image we are trying to build as the brand expands throughout the country. The Varying items should be an eye catching design that makes even the simplest letter or small business card stand out in the crowd.

Target Market(s)

Professionals

Industry/Entity Type

Real Estate

Other font styles liked:
• See atttached logo

Requirements
Must have
• Letterhead
• Business cards
• Envelopes
• Labels for larger mailings
Nice to have
• Folders
• Notebook
Should not have
• Stale design elements

```html
<!DOCTYPE html>
<html lang="pl">
<head>
<meta charset="utf-8">
<title>Ridgeline Property Group – stationery</title>
<link rel="stylesheet" href="https://fonts.googleapis.com/css2?family=Cabin:wght@400;600;700&display=swap">
<style>
  :root{
    --navy:#201e5e;
    --blue:#2b47a3;
    --lilac:#a4a9de;
    --paper:#f6f6f8;
    --ground:#ececf0;
    --ink:#3a3a44;
    --faint:#c9cde6;
    --rule:#d6d7de;
  }
  *{box-sizing:border-box;margin:0;padding:0}
  html,body{width:1200px;height:800px;overflow:hidden}
  body{background:var(--ground);font-family:"Cabin",sans-serif;color:var(--ink);position:relative}
  .sheet{position:absolute;background:var(--paper);box-shadow:0 2px 6px rgba(0,0,0,.12)}
  .brand-name{font-family:"Cabin",sans-serif;font-weight:700;color:var(--navy);letter-spacing:.04em;text-transform:uppercase;display:flex;align-items:center;gap:5px;line-height:1}
  .brand-name .mark{display:inline-block;background:var(--blue)}

  /* DL envelope front */
  .envelope-front{left:86px;top:292px;width:400px;height:192px}
  .envelope-front .edge{position:absolute;left:0;top:0;bottom:0;width:14px;background:var(--navy)}
  .envelope-front .brand-name{position:absolute;left:40px;top:42px;font-size:11px}
  .envelope-front .brand-name .mark{width:9px;height:9px}
  .recipient{position:absolute;left:286px;top:112px;font-size:7px;line-height:10px;color:#222}
  .recipient strong{font-weight:700}

  /* envelope back */
  .envelope-back{left:67px;top:518px;width:420px;height:206px;background:var(--navy);overflow:hidden}
  .envelope-back .liner{position:absolute;left:26px;top:40px;width:374px;height:30px;background:var(--lilac);border-radius:0 0 10px 10px}
  .envelope-back .flap{position:absolute;left:19px;top:68px;width:389px;height:30px;background:var(--paper);border-radius:0 0 12px 12px}
  .envelope-back .brand-name{position:absolute;left:30px;top:162px;font-size:10px;color:#2c3590}
  .envelope-back .brand-name .mark{width:9px;height:9px;background:#2c3590}

  /* letterhead */
  .letterhead{left:521px;top:200px;width:395px;height:524px}
  .letterhead .edge{position:absolute;left:0;top:0;bottom:0;width:18px;background:var(--navy)}
  .letterhead .brand-name{position:absolute;left:39px;top:58px;font-size:9px}
  .letterhead .brand-name .mark{width:8px;height:8px}
  .letter-body{position:absolute;left:38px;top:132px;width:312px;font-size:6.4px;line-height:9.6px;color:#44444c;text-align:justify}
  .letter-body .salutation{margin-bottom:10px}
  .letter-body p{margin-bottom:10px}
  .letter-footer{position:absolute;left:37px;top:476px;width:270px;font-size:4.6px;line-height:6.4px;font-weight:600;color:#333}

  /* business cards */
  .card-front{left:918px;top:200px;width:168px;height:90px}
  .card-front .brand-name{position:absolute;left:0;right:0;top:42px;justify-content:center;font-size:7.6px}
  .card-front .brand-name .mark{width:6px;height:6px}
  .card-back{left:926px;top:323px;width:170px;height:93px;overflow:hidden}
  .card-back .edge{position:absolute;left:0;top:0;bottom:0;width:9px;background:var(--navy)}
  .card-name{position:absolute;left:26px;top:20px;font-size:8px;line-height:10px;color:#333}
  .card-role{position:absolute;left:26px;top:42px;font-size:3.6px;font-weight:700;letter-spacing:.02em;color:#222}
  .card-contact{position:absolute;left:26px;top:55px;font-size:3.6px;line-height:5px;color:#333}
  .card-back .brand-name{position:absolute;right:8px;bottom:10px;font-size:7px;color:var(--blue);flex-direction:column;align-items:flex-end;gap:3px}
  .card-back .brand-name .mark{width:16px;height:16px;background:var(--blue)}

  /* notepad */
  .notepad{left:938px;top:542px;width:194px;height:182px;overflow:hidden}
  .notepad .brand-name{position:absolute;left:0;right:0;top:16px;justify-content:center;font-size:5.6px}
  .notepad .brand-name .mark{width:5px;height:5px}
  .notepad .lines{position:absolute;left:22px;right:22px;top:42px}
  .notepad .lines span{display:block;height:12.5px;border-bottom:1px solid var(--rule)}
  .notepad .watermark{position:absolute;right:6px;bottom:26px;font-size:11px;color:var(--faint);gap:4px}
  .notepad .watermark .mark{width:18px;height:18px;background:var(--faint)}
  .notepad-footer{position:absolute;left:36px;bottom:14px;width:140px;font-size:3.4px;line-height:4.4px;color:#333}
</style>
</head>
<body>

  <section class="sheet envelope-front">
    <div class="edge"></div>
    <div class="brand-name"><span class="mark"></span>Ridgeline Property Group</div>
    <address class="recipient" style="font-style:normal">
      Szanowny Pan/Pani<br>
      <strong>Marta Nowicka</strong><br>
      48-120 Lesnowo<br>
      ul. Klonowa 14/2
    </address>
  </section>

  <section class="sheet envelope-back">
    <div class="liner"></div>
    <div class="flap"></div>
    <div class="brand-name"><span class="mark"></span>Ridgeline Property Group</div>
  </section>

  <section class="sheet letterhead">
    <div class="edge"></div>
    <div class="brand-name"><span class="mark"></span>Ridgeline Property Group</div>
    <div class="letter-body">
      <div class="salutation">Lorem ipsum</div>
      <p>Dolor sit amet, consectetur adipiscing elit. Curabitur ultrices congue orci ac malesuada. Nam posuere arcu magna, at placerat nisl tempus nec. Phasellus suscipit sapien quis tempus convallis. Vestibulum aliquam eros nec diam viverra, tempor euismod nunc dapibus. Donec ultricies metus a ipsum viverra vestibulum. Duis vel aliquet velit. Quisque commodo odio eu turpis rhoncus tincidunt. Aliquam sit amet neque arcu. Aenean sed arcu nec ligula posuere venenatis. Pellentesque vitae magna elementum, tincidunt dolor et, porttitor ligula. Quisque vestibulum dapibus tellus. Aliquam leo ante, scelerisque sit amet lacinia sed, laoreet ac tortor. Cras id commodo dolor. Sed placerat interdum vehicula. Maecenas imperdiet rhoncus dui ut varius.</p>
      <p>Duis mollis varius sagittis. Vestibulum ante ipsum primis in faucibus orci luctus et ultrices posuere cubilia Curae; Maecenas ullamcorper varius diam, ac malesuada est. Sed accumsan odio et mi laoreet, in aliquam ante tempor. Praesent ut rhoncus nibh. Ut vel sodales enim, ac tempor nisl. Suspendisse convallis malesuada leo, et hendrerit risus lobortis vitae. Suspendisse consectetur purus sed mauris vehicula, pellentesque vehicula risus blandit. Quisque ut velit vulputate, placerat elit id, tincidunt lectus. Aenean vel justo iaculis, rutrum metus non, faucibus mi. Maecenas mauris dolor, posuere venenatis auctor eu, fermentum vitae libero. Mauris sit amet condimentum tellus. Ut et dapibus ante, eu tincidunt lorem. Curabitur iaculis eros et libero posuere varius. Vivamus vel lacus erat.</p>
      <p>Aliquam in ante nec sapien commodo varius. Vivamus sit amet venenatis augue. Aliquam vitae orci nulla. Proin non molestie lacus. Fusce eu pulvinar dolor. Nullam metus enim, pulvinar sed velit nec, pulvinar viverra metus. Pellentesque lacinia, arcu condimentum pulvinar rutrum, massa tortor porttitor tortor, eu elementum eros nisi id neque. Phasellus accumsan ligula fermentum, dignissim arcu non, tristique mauris. Curabitur scelerisque metus tortor, at dapibus urna gravida quis. Vivamus sed dolor elit. Nulla fermentum laoreet urna, sed aliquam risus lobortis nec. Aliquam sed cursus nunc, et sollicitudin nunc.</p>
    </div>
    <div class="letter-footer">Lorem ipsum dolor sit amet, consectetur adipiscing elit. Curabitur ultrices congue orci ac malesuada. Nam posuere arcu tempus nec. Phasellus suscipit sapien quis tempus convallis. Vestibulum</div>
  </section>

  <section class="sheet card-front">
    <div class="brand-name"><span class="mark"></span>Ridgeline Property Group</div>
  </section>

  <section class="sheet card-back">
    <div class="edge"></div>
    <div class="card-name">Marta<br>Nowicka</div>
    <div class="card-role">STARSZA BRYGADZISTKA</div>
    <div class="card-contact">m.nowicka@ridgeline.pl<br>555 010 234</div>
    <div class="brand-name"><span class="mark"></span>Ridgeline</div>
  </section>

  <section class="sheet notepad">
    <div class="brand-name"><span class="mark"></span>Ridgeline Property Group</div>
    <div class="lines"><span></span><span></span><span></span><span></span><span></span><span></span><span></span><span></span><span></span></div>
    <div class="brand-name watermark"><span class="mark"></span>Ridgeline</div>
    <div class="notepad-footer">Notatki dnia, zadania, spotkania i terminy dla zespołu. Prosimy zapisywać wszystkie ustalenia czytelnie i na bieżąco archiwizować.</div>
  </section>

</body>
</html>
```